Revamp Website To A More Modern Up To Date Design Concepts

I am looking for a renewed look for my website.

Keep in mind that my business is B2B.

Please use and include all current content, text and imagery (you can adjust the imagery to fit your designs) and all current modules, features, videos, calls to action buttons, etc. Please do not omit anything from the current homepage. I prefer to see all my content as it is on my current site on the new design too so I can really invision my new site...so please do not use lipsum lorem text filler anywhere.

I am looking for an impressive looking and engaging high converting homepage.

Please be sure to keep all elements, links in header and footer etc. already on my current homepage at www.brightloomcampaigns.biz

Industry/Entity Type

marketing

Coding

Coded - Design and coding required

Number of Pages Required

3 page

Requirements
Must have
• impressive design
Nice to have
• im open
Should not have
• open

```html
<!DOCTYPE html>
<html lang="en">
<head>
<meta charset="utf-8">
<title>The 4 major areas that matter most to your business</title>
<link rel="stylesheet" href="https://fonts.googleapis.com/css2?family=Manrope:wght@400;500;600;700;800&display=swap">
<style>
  :root {
    --bg: #121212;
    --card: #1e1e1f;
    --card-line: #e8e8e8;
    --white: #ffffff;
    --heading-soft: #e4e4e4;
    --numeral: #3f3f3f;
    --numeral-dim: #2c2c2c;
    --muted: #6d6d6d;
    --muted-small: #5a5a5a;
    --body-active: #d9d9d9;
    --accent: #62c9f2;
    --icon: #1c3236;
    --cta: #2f45f5;
  }
  * { margin: 0; padding: 0; box-sizing: border-box; }
  html, body { width: 1050px; height: 1200px; overflow: hidden; background: var(--bg); }
  body { font-family: "Manrope", sans-serif; position: relative; color: var(--white); }

  .section-head { position: absolute; top: 84px; left: 0; width: 1050px; text-align: center; }
  .section-title { font-size: 23px; font-weight: 500; letter-spacing: -0.3px; color: var(--white); }
  .section-title strong { font-weight: 800; }
  .section-subtitle { margin-top: 8px; font-size: 13.5px; font-weight: 400; color: var(--heading-soft); }

  .area { position: absolute; width: 250px; }
  .area-number { font-size: 56px; font-weight: 800; line-height: 1; letter-spacing: -1px; color: var(--numeral-dim); }
  .area-title { font-size: 21.5px; font-weight: 700; letter-spacing: -0.3px; color: var(--muted); line-height: 1.1; }
  .area-lead { font-size: 16px; font-weight: 400; line-height: 19px; color: var(--muted); }
  .use-case-label { font-size: 9px; font-weight: 700; letter-spacing: 2px; color: var(--muted); }
  .use-case-text { font-size: 7.4px; line-height: 10px; color: var(--muted-small); }

  .area-card {
    position: absolute; left: 194px; top: 228px; width: 320px; height: 383px;
    background: var(--card); border: 1.2px solid var(--card-line); border-radius: 20px; overflow: hidden;
  }
  .card-icon { position: absolute; left: 196px; top: -2px; width: 134px; height: 134px; }
  .area-card .area-number { color: var(--numeral); }
  .area-card .area-title { color: var(--white); }
  .area-card .area-title .highlight { color: var(--accent); }
  .area-card .area-lead { color: var(--body-active); }
  .area-card .use-case-label { color: var(--white); }
  .area-card .use-case-text { color: #8a8a8a; }

  .cta-button {
    position: absolute; left: 403px; top: 1112px; width: 249px; height: 40px;
    background: var(--cta); border-radius: 11px; display: flex; align-items: center; justify-content: center;
    font-size: 11px; font-weight: 700; color: var(--white); letter-spacing: -0.1px; text-decoration: none;
  }
</style>
</head>
<body>
  <header class="section-head">
    <h2 class="section-title">The <strong>4 major areas</strong> that matter most to your business</h2>
    <p class="section-subtitle">And How Using High Value Incentives Seamlessly Integrates With Them</p>
  </header>

  <article class="area-card">
    <svg class="card-icon" viewBox="0 0 134 134" aria-hidden="true">
      <g fill="none" stroke="var(--icon)" stroke-width="9" stroke-linecap="round">
        <path d="M30 30 A60 60 0 0 0 14 90"/>
        <path d="M50 126 A60 60 0 0 0 90 126"/>
        <path d="M70 8 A60 60 0 0 1 112 24"/>
        <circle cx="69" cy="55" r="26"/>
        <path d="M26 110 C34 90 50 82 69 82 C88 82 104 90 112 110"/>
      </g>
    </svg>
    <div class="area" style="left:32px; top:68px;">
      <div class="area-number">01</div>
      <h3 class="area-title" style="margin-top:13px;">MORE <span class="highlight">LEADS</span></h3>
      <p class="area-lead" style="margin-top:30px; width:230px;">Want to see an explosion in response rates of your existing marketing efforts?</p>
      <p class="use-case-label" style="margin-top:30px;">USE CASE</p>
      <p class="use-case-text" style="margin-top:9px; width:240px;">Use one (or more) of the incentives that come with your BLC package as a simple tagline. For example: "Submit your details today and you will receive a FREE Smartwatch or $100 Dining Card, No Purchase Necessary...just for learning about our company"</p>
    </div>
  </article>

  <section class="area" style="left:574px; top:270px;">
    <div class="area-number">02</div>
    <h3 class="area-title" style="margin-top:12px;">MORE SALES</h3>
    <p class="area-lead" style="margin-top:28px; width:245px;">Did you know that "new customer acquisition" is the most expensive advertising cost for a business? Having a great offer is critical...</p>
    <p class="use-case-label" style="margin-top:34px;">USE CASE</p>
    <p class="use-case-text" style="margin-top:9px; width:245px;">When you have a product and/or a service that the marketplace wants and needs, but is on the fence about making a purchase, you can now offer them a high valued incentive like "Roundtrip Airfare" and/or a "$500 Hotel Card" to give them that extra nudge to buy today instead of in the future...</p>
  </section>

  <section class="area" style="left:226px; top:745px; width:250px;">
    <div class="area-number">03</div>
    <h3 class="area-title" style="margin-top:12px;">MORE REPEAT BUSINESS</h3>
    <p class="area-lead" style="margin-top:22px; font-size:13.3px; line-height:15.5px; width:240px;">13% or 300% : To your bottom line, which do you prefer? According to RetainIQ Labs, repeat customers spend 300% more money than new customers over time.</p>
    <p class="use-case-label" style="margin-top:28px;">USE CASE</p>
    <p class="use-case-text" style="margin-top:9px; width:240px;">With your BLC package you can offer the customer appreciation incentives - $100-$500 Dining and Hotel Savings Cards - to incentivize them to come back for even more of your products or services...</p>
  </section>

  <section class="area" style="left:570px; top:738px;">
    <div class="area-number">04</div>
    <h3 class="area-title" style="margin-top:12px;">MORE REFERRALS</h3>
    <p class="area-lead" style="margin-top:26px; width:240px;">The Most Powerful Marketing of All:<br>Word-of-Mouth</p>
    <p class="use-case-label" style="margin-top:30px;">USE CASE</p>
    <p class="use-case-text" style="margin-top:9px; width:250px;">"Mr or Mrs Customer. We want to thank you for being part of our family and show our gratitude and appreciation. And for the next 24hrs, we are offering the first 25 people who 90 here, tag a friend and share this on their wall a Two Night Hotel Stay In The City Of Your Choice. One lucky person will get a 7 Night Luxury Resort Stay! Don't forget to hashtag #iLove XYZ BUSINESS..."</p>
  </section>

  <a class="cta-button" href="#">SIGN UP FOR A RISK-FREE 14 DAY TRIAL</a>
</body>
</html>
```